Exciting adult social quiz app needs awesome modern design

A new and exciting app for couples/sexual partners is in the making. It will be available for Korvix and Plume devices and allow one partner to invite another partner to the game. The partners will answer questions about their sexual desires and needs and then try to guess what the other one answered.

The app needs a high quality design and you can find some general inspiration in a similar social quiz app called "Pair Riddle" which can be found in Vela Shop and Runa Market. I like some of the basic layouts of this app.

The design should be classy and have a theme that matches the app subject. This is a sexual get-to-know-each-other-app and not a "porn app". I imagine colors might be black and red (not a requirement) and perhaps have some structures, pictures or backgrounds showing a bit of skin. It's important that the game can be accessed by players in the public space (e.g. in a bus, car etc.) without surroundings thinking it's a sex/porn game - but also important that it's exciting in a kind of sexual way. So try to find a fine line.

As the app is for both genders, the design should accommodate this.

Please see app mockups in the attached PDF.

Initially, please show design proposals for screens 13, 16 and 23.
Please notice that screen 16 doesn't have to be exactly those 2 bars - please make some alternative score comparison graphic in your proposal.

Looking forward to seeing your proposal soon!

Target Market(s)

Couples between 18 and 50

Industry/Entity Type

Adult

Requirements
Must have
• Smooth graphics like the app "Pair Riddle"
Nice to have
• Several proposals are appreciated. Perhaps you can show your proposals with different colors and object placements so that I can see some different options.

```html
<!DOCTYPE html>
<html lang="en">
<head>
<meta charset="utf-8">
<title>Velvet Duo – App Screens</title>
<link rel="stylesheet" href="https://fonts.googleapis.com/css2?family=Lilita+One&family=Nunito:wght@700;800;900&display=swap">
<style>
:root{
  --page:#ffffff;
  --wine-dark:#2a0303;
  --wine:#5a0808;
  --crimson:#7d0a0a;
  --red:#a81414;
  --red-bright:#c41c1c;
  --skin:#c98f72;
  --skin-dark:#6e3b2a;
  --gold:#d8c28a;
  --gold-dark:#a58a4a;
  --cream:#fff7c8;
  --title-ink:#2a0a00;
  --white:#ffffff;
  --ad-blue:#0a1cf0;
  --list-text:#7a0a0a;
}
*{box-sizing:border-box;margin:0;padding:0}
html,body{width:1200px;height:1000px;overflow:hidden;background:var(--page)}
body{position:relative;font-family:"Nunito",Arial,sans-serif}
.symbols{position:absolute;width:0;height:0}
.screen{position:absolute;width:280px;height:480px;overflow:hidden;background:linear-gradient(160deg,var(--wine) 0%,var(--wine-dark) 70%)}
.photo{position:absolute}
.photo-man{background:linear-gradient(180deg,#5a3a2c 0%,var(--skin) 45%,#4a2a20 100%);border-radius:0 0 0 30px}
.photo-woman{background:linear-gradient(90deg,#3a1a10 0%,var(--skin) 50%,var(--skin-dark) 100%);border-radius:0 40px 0 0}
.panel{position:absolute;background:linear-gradient(135deg,var(--crimson),var(--wine) 80%);box-shadow:0 0 10px rgba(0,0,0,.5)}
.band{position:absolute;left:0;width:280px;height:56px;background:linear-gradient(180deg,var(--red-bright),var(--crimson))}
.app-name{position:absolute;left:0;width:280px;text-align:center;font-family:"Nunito",sans-serif;font-weight:800;font-size:28px;line-height:40px;color:var(--white)}
.sym{position:absolute;color:#8c0e0e}
.card{position:absolute;left:32px;top:43px;width:216px;height:380px;background:linear-gradient(160deg,var(--red) 0%,var(--crimson) 45%,var(--wine) 100%);box-shadow:0 0 14px rgba(0,0,0,.6)}
.title{font-family:"Lilita One",sans-serif;color:var(--cream);text-align:center;white-space:nowrap;
  text-shadow:-2px -2px 0 var(--title-ink),2px -2px 0 var(--title-ink),-2px 2px 0 var(--title-ink),2px 2px 0 var(--title-ink),0 3px 4px rgba(0,0,0,.6)}
.card .title{position:absolute;left:0;width:216px;font-size:34px}
.hint{position:absolute;left:12px;width:192px;text-align:center;color:var(--white);font-weight:800;font-size:11.5px;line-height:1.45}
.hearts{position:absolute;left:10px;width:196px;display:flex;justify-content:space-between}
.hearts svg{width:44px;height:42px}
.btn{position:absolute;height:42px;border-radius:22px;background:linear-gradient(180deg,#f4f4f4,#b8b8b8);padding:5px;box-shadow:0 2px 4px rgba(0,0,0,.5)}
.btn span{display:block;height:100%;border-radius:17px;background:linear-gradient(180deg,#9a0c0c,#4a0000);color:var(--white);font-weight:900;font-size:15px;text-align:center;line-height:32px}
.header{position:absolute;left:0;top:0;width:280px;height:52px;background:linear-gradient(180deg,var(--red),var(--crimson));border-bottom:2px solid #e6c48a}
.header .title{line-height:52px;font-size:34px}
.header .title.small{font-size:28px}
.header .title.smaller{font-size:23px}
.body-red{background:linear-gradient(160deg,#8e2020 0%,var(--crimson) 50%,#6a0808 100%)}
.ads{position:absolute;left:45px;bottom:3px;width:196px;height:26px;background:var(--ad-blue);color:var(--white);font-weight:900;font-size:15px;text-align:center;line-height:26px}
.collect{position:absolute;left:15px;top:68px;width:250px;height:374px;border-radius:40px;background:linear-gradient(180deg,#e8d4a4 0%,var(--gold) 60%,var(--gold-dark) 100%);box-shadow:0 0 8px rgba(0,0,0,.5)}
.collect-head{position:absolute;left:0;top:0;width:250px;height:80px;border-radius:40px 40px 0 0;background:linear-gradient(180deg,#d8b0a8,#e8d4a4)}
.collect-title{position:absolute;left:0;top:40px;width:250px;text-align:center;font-family:"Lilita One",sans-serif;font-size:22px;color:var(--crimson)}
.figure-icon{position:absolute;left:98px;top:6px;width:56px;height:34px;background:var(--crimson);border-radius:50% 50% 30% 30%;opacity:.9}
.favours{position:absolute;left:5px;top:79px;width:232px;list-style:none}
.favours li{height:56px;margin-bottom:2px;background:linear-gradient(180deg,#ffffff,#f0d6d6);border:1px solid #d9b0b0;color:var(--list-text);font-weight:900;font-size:14px;line-height:1.2;padding:8px 6px;display:flex;align-items:center}
.scroll{position:absolute;left:237px;top:79px;width:12px;height:230px;background:#f4eea4;border:1px solid #b89c4a}
.scroll i{position:absolute;left:2px;top:12px;width:6px;height:36px;background:#b07a2a}
.lead{position:absolute;left:0;width:280px;text-align:center;color:var(--white);font-weight:900;font-size:15px;line-height:1.35}
.avatar{position:absolute;border-radius:50%;background:radial-gradient(circle at 50% 40%,#9aa6b4,#4e5a66);border:4px solid var(--red);box-shadow:0 0 0 2px #4a0000}
.avatar.her{background:radial-gradient(circle at 50% 40%,#8a6a5a,#3a2a26)}
.silhouette{position:absolute;border-radius:30px 8px 8px 30px}
.sil-one{background:linear-gradient(90deg,#e01a1a 0%,#e01a1a 40%,#f3e6e0 60%,#f3e6e0 100%)}
.sil-two{background:linear-gradient(90deg,#f03030 0%,#e01a1a 55%,#f3e6e0 75%,#f3e6e0 100%)}
.stage{position:absolute;left:0;top:52px;width:280px;background:radial-gradient(ellipse at 60% 50%,#a05050 0%,#8a3434 55%,#7a2424 100%)}
.answers{position:absolute;left:0;top:290px;width:280px;height:163px;background:#f4eeee;padding:6px 5px;display:flex;flex-direction:column;gap:6px}
.answers div{height:45px;background:var(--crimson);color:var(--white);font-weight:900;font-style:italic;font-size:16px;text-align:center;line-height:45px}
.footer-band{position:absolute;left:0;top:453px;width:280px;height:27px;background:#7a3a3a}
.said{position:absolute;left:0;width:280px;text-align:center;color:var(--white);font-weight:900;font-size:15px}
.nudge{position:absolute;left:58px;top:72px;width:190px;height:74px;background:linear-gradient(160deg,var(--red),var(--wine));box-shadow:2px 3px 6px rgba(0,0,0,.6);color:var(--white);font-weight:900;font-size:22px;line-height:74px;text-align:center;padding-left:14px}
.player-name{position:absolute;color:var(--white);font-weight:900;font-size:13px}
.divider{position:absolute;left:28px;width:224px;height:2px;background:linear-gradient(90deg,transparent,#e6c48a,transparent)}
.chat-title{position:absolute;left:0;width:280px;font-size:24px}
.bubble{position:absolute;height:26px;border-radius:13px;background:#f1e4e4;color:#2a0a0a;font-weight:900;font-size:14px;line-height:26px;text-align:center}
.chat-input{position:absolute;left:12px;top:408px;width:255px;height:32px;background:rgba(240,220,220,.35);border:1px solid #c49a9a;color:rgba(255,255,255,.45);font-weight:800;font-size:14px;line-height:30px;padding-left:8px}
</style>
</head>
<body>

<svg class="symbols" aria-hidden="true">
  <defs>
    <symbol id="male" viewBox="0 0 60 50"><circle cx="18" cy="32" r="14" fill="none" stroke="currentColor" stroke-width="4"/><line x1="28" y1="22" x2="54" y2="6" stroke="currentColor" stroke-width="4"/><path d="M40 2 L58 3 L52 18 Z" fill="currentColor"/></symbol>
    <symbol id="female" viewBox="0 0 40 64"><circle cx="20" cy="18" r="14" fill="none" stroke="currentColor" stroke-width="4"/><line x1="20" y1="32" x2="20" y2="62" stroke="currentColor" stroke-width="4"/><line x1="8" y1="48" x2="32" y2="48" stroke="currentColor" stroke-width="4"/></symbol>
    <symbol id="heart" viewBox="0 0 44 42"><path d="M22 41 C10 30 1 22 1 12 C1 5 6 1 12 1 C17 1 20 4 22 8 C24 4 27 1 32 1 C38 1 43 5 43 12 C43 22 34 30 22 41 Z" fill="#d81c1c"/></symbol>
  </defs>
</svg>

<!-- Splash -->
<section class="screen" style="left:10px;top:14px">
  <div class="panel" style="left:32px;top:43px;width:248px;height:170px"></div>
  <div class="photo photo-man" style="left:196px;top:0;width:84px;height:210px" role="img" aria-label="Photo of a bare male torso"></div>
  <svg class="sym" style="left:40px;top:62px;width:68px;height:56px"><use href="#male"/></svg>
  <div class="band" style="top:211px"></div>
  <div class="app-name" style="top:219px">Velvet Duo</div>
  <div class="panel" style="left:62px;top:267px;width:196px;height:158px"></div>
  <div class="photo photo-woman" style="left:0;top:267px;width:92px;height:213px" role="img" aria-label="Photo of a woman seen from behind"></div>
  <svg class="sym" style="left:206px;top:350px;width:34px;height:64px"><use href="#female"/></svg>
</section>

<!-- Create PIN -->
<section class="screen" style="left:309px;top:14px">
  <div class="photo photo-man" style="left:196px;top:0;width:84px;height:210px" role="img" aria-label="Photo of a bare male torso"></div>
  <div class="band" style="top:211px"></div>
  <div class="photo photo-woman" style="left:0;top:267px;width:92px;height:213px" role="img" aria-label="Photo of a woman seen from behind"></div>
  <div class="card">
    <svg class="sym" style="left:8px;top:12px;width:68px;height:56px"><use href="#male"/></svg>
    <div class="title" style="top:62px">Welcome</div>
    <p class="hint" style="top:124px">Please create a PIN so that only you can access the app:</p>
    <div class="hearts" style="top:170px">
      <svg><use href="#heart"/></svg><svg><use href="#heart"/></svg><svg><use href="#heart"/></svg><svg><use href="#heart"/></svg>
    </div>
    <div class="btn" style="left:38px;top:254px;width:140px"><span>Continue</span></div>
    <svg class="sym" style="left:172px;top:306px;width:34px;height:64px"><use href="#female"/></svg>
  </div>
</section>

<!-- Input PIN -->
<section class="screen" style="left:608px;top:14px">
  <div class="photo photo-man" style="left:196px;top:0;width:84px;height:210px" role="img" aria-label="Photo of a bare male torso"></div>
  <div class="band" style="top:211px"></div>
  <div class="photo photo-woman" style="left:0;top:267px;width:92px;height:213px" role="img" aria-label="Photo of a woman seen from behind"></div>
  <div class="card">
    <svg class="sym" style="left:8px;top:12px;width:68px;height:56px"><use href="#male"/></svg>
    <div class="title" style="top:96px">Input PIN</div>
    <div class="hearts" style="top:172px">
      <svg><use href="#heart"/></svg><svg><use href="#heart"/></svg><svg><use href="#heart"/></svg><svg><use href="#heart"/></svg>
    </div>
    <div class="btn" style="left:38px;top:254px;width:140px"><span>Continue</span></div>
    <svg class="sym" style="left:172px;top:306px;width:34px;height:64px"><use href="#female"/></svg>
  </div>
</section>

<!-- Round 1: collect favour -->
<section class="screen body-red" style="left:907px;top:14px">
  <header class="header"><div class="title">Round 1</div></header>
  <div class="collect">
    <div class="collect-head"></div>
    <div class="figure-icon" role="img" aria-label="Silhouette icon of a reclining figure"></div>
    <div class="collect-title">Time to collect!</div>
    <ul class="favours">
      <li>Oral... Tonight!</li>
      <li>Be naked when i come home tomorrow</li>
      <li>Naked back massage with oil</li>
      <li>Naked foot massage</li>
    </ul>
    <div class="scroll"><i></i></div>
    <div class="btn" style="left:55px;top:318px;width:140px"><span>Continue</span></div>
  </div>
  <div class="ads">Ads here</div>
</section>

<!-- Round 1: winner -->
<section class="screen body-red" style="left:10px;top:507px">
  <header class="header"><div class="title">Round 1</div></header>
  <p class="lead" style="top:74px">Winner of the round<br>selects a sexual favour</p>
  <div class="avatar" style="left:18px;top:146px;width:46px;height:46px"></div>
  <svg class="sym" style="left:58px;top:128px;width:50px;height:42px;color:var(--red)"><use href="#male"/></svg>
  <div class="silhouette sil-one" style="left:120px;top:138px;width:152px;height:44px" role="img" aria-label="Silhouette of a man lying down"></div>
  <div class="avatar her" style="left:16px;top:224px;width:46px;height:46px"></div>
  <svg class="sym" style="left:22px;top:262px;width:34px;height:50px;color:var(--red)"><use href="#female"/></svg>
  <div class="silhouette sil-two" style="left:122px;top:212px;width:146px;height:52px" role="img" aria-label="Silhouette of a woman lying down"></div>
  <div class="btn" style="left:76px;top:391px;width:136px"><span>Continue</span></div>
  <div class="ads">Ads here</div>
</section>

<!-- Guessing time -->
<section class="screen" style="left:309px;top:507px">
  <header class="header"><div class="title small">Guessing time</div></header>
  <div class="stage" style="height:238px"></div>
  <p class="lead" style="top:82px">Do you enjoy giving<br>oral sex?</p>
  <div class="avatar" style="left:120px;top:192px;width:40px;height:40px"></div>
  <svg class="sym" style="left:154px;top:172px;width:46px;height:38px;color:var(--red)"><use href="#male"/></svg>
  <div class="said" style="top:256px">Said:</div>
  <div class="answers"><div>Hell yeah</div><div>I guess</div><div>No</div></div>
  <div class="footer-band"></div>
  <div class="ads">Ads here</div>
</section>

<!-- Answering time -->
<section class="screen" style="left:608px;top:507px">
  <header class="header"><div class="title small">Answering time</div></header>
  <div class="stage" style="height:238px"></div>
  <div class="avatar" style="left:102px;top:98px;width:64px;height:64px"></div>
  <svg class="sym" style="left:150px;top:62px;width:84px;height:70px;color:var(--red)"><use href="#male"/></svg>
  <p class="lead" style="top:220px">Do you enjoy giving<br>oral sex?</p>
  <div class="answers"><div>Hell yeah</div><div>I guess</div><div>No</div></div>
  <div class="footer-band"></div>
  <div class="ads">Ads here</div>
</section>

<!-- Waiting + chat -->
<section class="screen body-red" style="left:907px;top:507px">
  <header class="header"><div class="title smaller">Waiting for your turn</div></header>
  <div class="player-name" style="left:34px;top:60px">Mira</div>
  <div class="nudge">Send nudge</div>
  <div class="avatar her" style="left:28px;top:80px;width:44px;height:44px"></div>
  <svg class="sym" style="left:34px;top:118px;width:32px;height:50px;color:var(--red)"><use href="#female"/></svg>
  <div class="divider" style="top:183px"></div>
  <div class="title chat-title" style="top:168px">Chat</div>
  <div class="avatar her" style="left:20px;top:212px;width:38px;height:38px"></div>
  <svg class="sym" style="left:24px;top:244px;width:30px;height:44px;color:var(--red)"><use href="#female"/></svg>
  <div class="bubble" style="left:70px;top:220px;width:190px">We can chat here!</div>
  <div class="bubble" style="left:108px;top:287px;width:92px">Cool!</div>
  <div class="avatar" style="left:208px;top:282px;width:38px;height:38px"></div>
  <svg class="sym" style="left:236px;top:262px;width:42px;height:36px;color:var(--red)"><use href="#male"/></svg>
  <div class="chat-input">Chat text here</div>
  <div class="ads">Ads here</div>
</section>

</body>
</html>
```